Business Card Design Project for - The Pellowick Greenworks Company Ltd. We are a Landscape and garden

I would like designer to use all special glosses etc so i can have a professional looking business card. The theme of the business card can reflect that of the Logo attached by MarkQuarry or your own unique ideas.. please feel free to go wild as i hope i can select a winner i like - my budget will be committed so please get involved. Good luck and thank you Lyndon

Target Market(s)

Must look Professional

General Public and Businesses including Councils, Local Government, Hospitals, Hotels, Professionals and Professional Sports People.

Industry/Entity Type

Landscape Gardening

Contact Information for Business Card

The Pellowick Greenworks Company Ltd

Mr L.R Ashcombe
Head Office - Quayfront Park Manchester
t. 0772 408 916
e. info@pellowickgreenworks.co.uk
w. www.pellowickgreenworks.co.uk

Facebook - https://www.friendpage-example.com/ThePellowickGreenworksCompany/
Twitter - https://chirpline-example.com/ThePruningCart
Instagram - https://www.snapgrid-example.com/thepellowickgreenworkscompany/?hl=en
Google+ - https://circles.searchhub-example.com/u/0/208473950162438571093
Yelp - https://www.reviewnook-example.co.uk/biz/the-pellowick-greenworks-company-manchester-4

Font styles to use
Serif
Script
Other font styles liked:
• I don't have much of an idea of font types sorry

Colors

Designer to choose colors to be used in the design.

Requirements
Must have
• A Professional look and Design
• Special effects with gloss and fading of colours possibly..
• Front and back design
Nice to have
• All special features with effects and gloss etc

```html
<!DOCTYPE html>
<html lang="en">
<head>
<meta charset="utf-8">
<title>The Pellowick Greenworks Company Ltd — Business Card</title>
<link rel="stylesheet" href="https://fonts.googleapis.com/css2?family=Cinzel:wght@400&family=Josefin+Sans:wght@400;600&display=swap">
<style>
  :root {
    --page: #ececec;
    --card-dark: #1c1c1c;
    --card-light: #ffffff;
    --brand-grey: #9a9a9a;
    --ink: #1a1a1a;
    --green: #4cbb2f;
    --icon-grey: #8a8a8a;
    --faint: #ececec;
  }
  * { box-sizing: border-box; margin: 0; padding: 0; }
  html, body { width: 1200px; height: 1200px; overflow: hidden; background: var(--page); }
  .canvas { position: relative; width: 1200px; height: 1200px; }

  .card {
    position: absolute; left: 370px; width: 460px; height: 276px;
    background: var(--card-dark); overflow: hidden;
  }
  .card--back { top: 176px; }
  .card--front { top: 672px; }

  .brand { position: absolute; text-align: center; font-family: "Cinzel", serif; font-weight: 400; color: var(--brand-grey); }
  .brand__dot { display: block; margin: 0 auto 12px; width: 36px; height: 36px; border-radius: 50%; background: var(--green); }
  .brand__name { display: block; font-size: 25px; letter-spacing: 2px; line-height: 1; }
  .brand__line { display: block; font-size: 9px; letter-spacing: 2.2px; margin-top: 10px; }

  .card--back .brand { left: 0; right: 0; top: 38px; }

  .social { position: absolute; left: 100px; top: 190px; list-style: none; }
  .social li { display: flex; align-items: center; height: 13px; font-family: "Josefin Sans", sans-serif; font-size: 6.3px; color: var(--green); }
  .social .dot { width: 7px; height: 7px; border-radius: 50%; background: var(--icon-grey); margin-right: 9px; flex: none; }

  .front__panel { position: absolute; inset: 0; }
  .person { position: absolute; left: 17px; top: 22px; font-family: "Josefin Sans", sans-serif; color: var(--ink); }
  .person__name { font-size: 17px; font-weight: 400; }
  .person__role { font-size: 8px; font-weight: 600; margin-top: 5px; }

  .card--front .brand { left: 190px; width: 284px; top: 36px; }
  .card--front .brand__name { font-size: 19px; }
  .card--front .brand__dot { width: 30px; height: 30px; margin-bottom: 10px; }
  .card--front .brand__line { font-size: 7.5px; margin-top: 9px; }

  .contact { position: absolute; left: 160px; top: 186px; list-style: none; font-family: "Josefin Sans", sans-serif; font-size: 12.5px; color: var(--green); letter-spacing: .3px; }
  .contact li { display: flex; align-items: center; height: 20px; }
  .contact svg { width: 11px; height: 11px; margin-right: 7px; flex: none; }
</style>
</head>
<body>
<div class="canvas">

  <section class="card card--back" aria-label="Card back">
    <div class="brand">
      <span class="brand__dot"></span>
      <span class="brand__name">THE PELLOWICK</span>
      <span class="brand__line">GREENWORKS COMPANY LTD</span>
    </div>
    <ul class="social">
      <li><span class="dot"></span>https://www.friendpage-example.com/ThePellowickGreenworksCompany/</li>
      <li><span class="dot"></span>https://chirpline-example.com/ThePruningCart</li>
      <li><span class="dot"></span>https://www.snapgrid-example.com/thepellowickgreenworkscompany/?hl=en</li>
      <li><span class="dot"></span>https://circles.searchhub-example.com/u/0/208473950162438571093</li>
      <li><span class="dot"></span>https://www.reviewnook-example.co.uk/biz/the-pellowick-greenworks-company-manchester-4</li>
    </ul>
  </section>

  <section class="card card--front" aria-label="Card front">
    <svg class="front__panel" width="460" height="276" viewBox="0 0 460 276" aria-hidden="true">
      <polygon points="0,0 230,0 120,276 0,276" fill="var(--card-light)"/>
      <clipPath id="light-area"><polygon points="0,0 230,0 120,276 0,276"/></clipPath>
      <circle cx="70" cy="170" r="85" fill="var(--faint)" clip-path="url(#light-area)"/>
    </svg>
    <div class="person">
      <div class="person__name">Mr L.R Ashcombe</div>
      <div class="person__role">Head Office - Quayfront Park Manchester</div>
    </div>
    <div class="brand">
      <span class="brand__dot"></span>
      <span class="brand__name">THE PELLOWICK</span>
      <span class="brand__line">GREENWORKS COMPANY LTD</span>
    </div>
    <ul class="contact">
      <li>
        <svg viewBox="0 0 24 24" aria-hidden="true"><path fill="var(--green)" d="M6.6 10.8a15.1 15.1 0 0 0 6.6 6.6l2.2-2.2c.3-.3.7-.4 1-.2 1.1.4 2.3.6 3.6.6.6 0 1 .4 1 1V20c0 .6-.4 1-1 1A17 17 0 0 1 3 4c0-.6.4-1 1-1h3.5c.6 0 1 .4 1 1 0 1.3.2 2.5.6 3.6.1.3 0 .7-.2 1z"/></svg>
        0772 408 916
      </li>
      <li>
        <svg viewBox="0 0 24 24" aria-hidden="true"><rect x="2.5" y="5" width="19" height="14" fill="none" stroke="var(--green)" stroke-width="2.4"/><path d="M3 6l9 7 9-7" fill="none" stroke="var(--green)" stroke-width="2.4"/></svg>
        info@pellowickgreenworks.co.uk
      </li>
      <li>
        <svg viewBox="0 0 24 24" aria-hidden="true"><g fill="none" stroke="var(--green)" stroke-width="2.2"><circle cx="12" cy="12" r="9.5"/><ellipse cx="12" cy="12" rx="4" ry="9.5"/><path d="M2.5 12h19"/></g></svg>
        www.pellowickgreenworks.co.uk
      </li>
    </ul>
  </section>

</div>
</body>
</html>
```